New Infographic Design Project

I need a 1 page Infographic that explains our Quillstone Prism offer.

Can you use the following content in the attached document to create a 1 page infographic. The image in the bottom of the document is one of our competitors who is offering the same thing, this image is only provided for inspiration and ideas as we need ours to be based on the content of the document and aligned with the Corvenly Brand

```html
<!DOCTYPE html>
<html lang="en">
<head>
<meta charset="utf-8">
<title>Data Ready. AI Ready. In 6 Weeks.</title>
<link href="https://fonts.googleapis.com/css2?family=Montserrat:wght@400;500;700;800;900&display=swap" rel="stylesheet">
<style>
  :root{
    --navy:#0b1f4d;
    --navy-deep:#091a40;
    --panel:#0c2454;
    --card:#3a72b8;
    --sky:#5bbcea;
    --white:#ffffff;
    --w1:#5bbcea;
    --w2:#d86a6f;
    --w3:#d9a83a;
    --w4:#5aaaa8;
    --w5:#8e6adb;
    --w6:#ee7f3a;
  }
  *{box-sizing:border-box;margin:0;padding:0}
  html,body{width:1200px;height:678px;overflow:hidden;background:var(--navy)}
  body{font-family:"Montserrat",Arial,sans-serif;color:var(--white)}
  .infographic{position:relative;width:1200px;height:678px;overflow:hidden}
  .backdrop{position:absolute;inset:0;background:
    radial-gradient(ellipse at 40% 35%,#2a62ad 0%,rgba(30,80,160,.6) 35%,rgba(11,31,77,0) 75%),
    linear-gradient(135deg,#123a7c 0%,#1c4f9a 45%,#143d82 100%)}
  .title-band{position:absolute;left:0;top:0;width:1200px;height:73px;background:var(--navy)}
  .title{position:absolute;left:41px;top:12px;font-weight:900;font-size:46px;letter-spacing:.5px;line-height:1;white-space:nowrap}
  .title .accent{color:var(--sky)}

  .intro{position:absolute;left:36px;top:98px;width:560px}
  .intro h2{font-size:12.2px;font-weight:800;letter-spacing:.1px;margin-bottom:4px}
  .intro p{font-size:12.4px;font-weight:500;line-height:20px}

  .edge{position:absolute;left:626px;top:82px;width:557px;height:180px;background:var(--panel);border-radius:23px;padding:11px 20px 0 15px}
  .edge h2{font-size:12.4px;font-weight:800;color:var(--sky);margin-bottom:3px}
  .edge ul{list-style:none}
  .edge li{position:relative;padding-left:22px;font-size:12.4px;line-height:17.5px;font-weight:500}
  .edge li::before{content:"";position:absolute;left:10px;top:7px;width:4px;height:4px;border-radius:50%;background:var(--white)}
  .edge strong{font-weight:800}

  .timeline-banner{position:absolute;left:0;top:234px}
  .timeline-banner .label{position:absolute;left:73px;top:6px;font-size:28px;font-weight:900;color:var(--sky);white-space:nowrap;letter-spacing:.3px}
  .timeline-banner .icon{position:absolute;left:34px;top:8px}

  .week{position:absolute;top:328px;width:154px;height:217px;background:var(--card);border-radius:20px;text-align:center}
  .week .badge{position:absolute;left:37px;top:-42px;width:80px;height:80px;border-radius:50%;display:flex;flex-direction:column;align-items:center;justify-content:center;line-height:1}
  .week .badge small{font-size:11px;font-weight:800;margin-top:4px}
  .week .badge b{font-size:29px;font-weight:900;margin-top:-1px}
  .week h3{position:absolute;top:48px;left:4px;right:4px;font-size:11.4px;font-weight:800;line-height:15px}
  .week p{position:absolute;top:89px;left:8px;right:8px;font-size:10.6px;font-weight:500;line-height:14.7px}
  .week .arrow{position:absolute;left:154px;top:84px}

  .w1{left:34px}.w1 .badge{background:var(--w1)}
  .w2{left:227px}.w2 .badge{background:var(--w2)}
  .w3{left:419px}.w3 .badge{background:var(--w3)}
  .w4{left:611px}.w4 .badge{background:var(--w4)}
  .w5{left:804px}.w5 .badge{background:var(--w5)}
  .w6{left:997px}.w6 .badge{background:var(--w6)}

  .promise-band{position:absolute;left:0;top:558px}
  .promise{position:absolute;top:570px;text-align:center}
  .promise .pill{display:inline-block;height:25px;line-height:25px;border-radius:13px;padding:0 10px;font-size:13px;font-weight:800;white-space:nowrap}
  .promise p{margin-top:19px;font-size:11.5px;font-weight:500;line-height:15.6px}
  .p1{left:26px;width:208px}.p1 .pill{background:var(--w5)}
  .p2{left:244px;width:200px}.p2 .pill{background:var(--w2)}
  .p3{left:467px;width:180px}.p3 .pill{background:var(--w3)}
  .p4{left:662px;width:180px}.p4 .pill{background:var(--w4)}
</style>
</head>
<body>
<main class="infographic">
  <div class="backdrop" role="img" aria-label="Deep blue digital data stream background"></div>

  <header class="title-band">
    <h1 class="title">DATA READY. AI READY. <span class="accent">IN 6 WEEKS.</span></h1>
  </header>

  <section class="intro">
    <h2>YOUR LONG-TERM STRATEGIC DATA PARTNER</h2>
    <p>We start with a Business Data Assessment or Prism Deployment Assessment to pinpoint the highest-value use cases, the biggest data risks, and the fastest path to impact. We stand up a governed Quillstone Prism foundation using repeatable ingestion, validation, and common data model patterns, so your reporting scales cleanly and your AI initiatives provide business value.</p>
  </section>

  <section class="edge">
    <h2>THE CORVENLY EDGE</h2>
    <ul>
      <li><strong>Quality-first delivery</strong> Automated validation, data tests, and “quality gates” that stop bad data upstream.</li>
      <li><strong>Data products, not datasets</strong> Clear ownership, SLAs, versioning, and reusable, consumable outputs aligned to high impact business outcomes.</li>
      <li><strong>Governance that doesn’t slow you down</strong> Security, access, lineage, and auditability built in from day one.</li>
      <li><strong>Operate seamlessly</strong> CI/CD, monitoring, and cost controls so the platform stays healthy.</li>
    </ul>
  </section>

  <div class="timeline-banner">
    <svg width="450" height="45" viewBox="0 0 450 45" aria-hidden="true"><polygon points="0,0 418,0 446,22.5 418,45 0,45" fill="var(--navy-deep)"/></svg>
    <svg class="icon" width="30" height="30" viewBox="0 0 30 30" aria-hidden="true">
      <rect x="2" y="5" width="26" height="23" rx="3" fill="none" stroke="#fff" stroke-width="2"/>
      <line x1="2" y1="11" x2="28" y2="11" stroke="#fff" stroke-width="2"/>
      <line x1="9" y1="2" x2="9" y2="7" stroke="#fff" stroke-width="2"/>
      <line x1="15" y1="2" x2="15" y2="7" stroke="#fff" stroke-width="2"/>
      <line x1="21" y1="2" x2="21" y2="7" stroke="#fff" stroke-width="2"/>
      <polyline points="10,19 14,23 21,15" fill="none" stroke="#fff" stroke-width="2"/>
    </svg>
    <span class="label">6 WEEK TIME TO VALUE</span>
  </div>

  <article class="week w1">
    <div class="badge"><small>WEEK</small><b>01</b></div>
    <h3>Envision<br>&amp; Assess</h3>
    <p>Use case shortlist and priority based on highest business impact, current-state review, data risk &amp; compliance priorities, target operating model.</p>
    <svg class="arrow" width="26" height="82" aria-hidden="true"><polygon points="0,0 25,41 0,82" fill="var(--w1)"/></svg>
  </article>
  <article class="week w2">
    <div class="badge"><small>WEEK</small><b>02</b></div>
    <h3>Architecture &amp;<br>governance design</h3>
    <p>Landing zone decisions, security and access model, patterns/standards, delivery plan and success metrics.</p>
    <svg class="arrow" width="26" height="82" aria-hidden="true"><polygon points="0,0 25,41 0,82" fill="var(--w2)"/></svg>
  </article>
  <article class="week w3">
    <div class="badge"><small>WEEK</small><b>03</b></div>
    <h3>Prism foundation<br>deployed</h3>
    <p>Workspaces and environments, automation &amp; CI/CD, onboarding playbooks, baseline policies/guardrails.</p>
    <svg class="arrow" width="26" height="82" aria-hidden="true"><polygon points="0,0 25,41 0,82" fill="var(--w3)"/></svg>
  </article>
  <article class="week w4">
    <div class="badge"><small>WEEK</small><b>04</b></div>
    <h3>Data ingestion +<br>validation framework</h3>
    <p>Reusable ingestion patterns, automated validation, data contracts/SLAs, observability signals and alerting.</p>
    <svg class="arrow" width="26" height="82" aria-hidden="true"><polygon points="0,0 25,41 0,82" fill="var(--w4)"/></svg>
  </article>
  <article class="week w5">
    <div class="badge"><small>WEEK</small><b>05</b></div>
    <h3>Scalable common<br>data model</h3>
    <p>Domain model, master entities, curated layer, semantic modelling patterns that support Lumagraph at scale.</p>
    <svg class="arrow" width="26" height="82" aria-hidden="true"><polygon points="0,0 25,41 0,82" fill="var(--w5)"/></svg>
  </article>
  <article class="week w6">
    <div class="badge"><small>WEEK</small><b>06</b></div>
    <h3>Business outcomes +<br>AI-ready capability</h3>
    <p>Executive dashboards and priority reports, performance optimisation, hypercare and handover, AI readiness check and pilot plan (predictive analytics and/or secure enterprise LLM).</p>
    <svg class="arrow" width="26" height="82" aria-hidden="true"><polygon points="0,0 25,41 0,82" fill="var(--w6)"/></svg>
  </article>

  <svg class="promise-band" width="910" height="120" viewBox="0 0 910 120" aria-hidden="true"><polygon points="0,0 855,0 904,64 855,120 0,120" fill="var(--navy)"/></svg>

  <div class="promise p1"><span class="pill">“AI-ready data” guarantee</span><p>Every priority dataset ships with validation rules, ownership, lineage, and freshness SLAs before it can power AI.</p></div>
  <div class="promise p2"><span class="pill">Cost-to-serve transparency</span><p>Show business owners what each product/report costs to run and optimise it continuously.</p></div>
  <div class="promise p3"><span class="pill">Change-proof pipelines</span><p>Data contracts + automated tests reduce breakages from upstream schema changes. Governed self-serve</p></div>
  <div class="promise p4"><span class="pill">Governed self-serve</span><p>Catalog + certified datasets so teams move faster without creating data chaos.</p></div>
</main>
</body>
</html>
```